Driving-coach/trainer who wants to inform about the offer and how I can help people to drive more re

I need a flyer that informs potential customers about my offer.

DL size 210 mm x 99 mm, vertical!

I'm a trainer/coach who helps people to drive a car more relaxed, without fear and more confident.

It's a one to one training. I do train people in their own car. It gets people their freedom back to go where and when they like to go by own car...
Updates

Project Deadline Extended Reason: I would like to extend my project... didn't find the time to give feedback because of unexpected other jobs I had to do.Would be great if you could extend my project around 5 more days. THANKS. Added Wednesday, January 4, 2017

Target Market(s)

People (man an woman) who are afraid of driving a car, or are very stressed while driving....

Industry/Entity Type

Life Coaching

Font styles to use
Sans Serif

Colors
acd136

Requirements
Must have
• Page 1:
• -my offer (see text-pdf)
• -three fotos (see attached files "Pixavine") of people who are satisfied with my offer
• Page 2:
• -advantages in the work with me.
• -contact information
• -and a picture of me (see attached file) next to the contact information or the advantages of my work
• -my logo (see attached file) on Page 1 + 2
• -i like a "clear" and structured layout. "Less is more"

```html
<!DOCTYPE html>
<html lang="de">
<head>
<meta charset="utf-8">
<title>Fahrangst-Coaching Flyer</title>
<link rel="stylesheet" href="https://fonts.googleapis.com/css2?family=Advent+Pro:wght@300;400&family=Josefin+Sans:wght@300&display=swap">
<style>
  :root {
    --page: #9c9393;
    --gap: #ffffff;
    --ink: #161616;
    --accent: #b4dc48;
    --headline: #eef23c;
    --frame: #1b1b1b;
  }
  * { box-sizing: border-box; margin: 0; padding: 0; }
  html, body { width: 1194px; height: 1200px; overflow: hidden; background: var(--gap); }
  body { position: relative; font-family: "Advent Pro", "Arial Narrow", sans-serif; color: var(--ink); }
  .panel { position: absolute; top: 0; height: 1200px; background: var(--page); }
  .panel--front { left: 0; width: 566px; }
  .panel--back { left: 629px; width: 565px; }
  .frame { position: absolute; border: 2px solid var(--frame); }
  .panel--front .frame { left: 14px; top: 14px; width: 538px; height: 1167px; }
  .panel--back .frame { left: 13px; top: 14px; width: 538px; height: 1167px; }
  .hero {
    position: absolute; left: 0; top: 0; width: 566px; height: 340px;
    background: linear-gradient(180deg, #8a8fbd 0%, #8e93b4 22%, #8f9a83 42%, #a9a64e 62%, #a59b7c 80%, var(--page) 100%);
  }
  .block { position: absolute; font-size: 21px; line-height: 25px; font-weight: 400; }
  .hl { color: var(--accent); }
  .headline { left: 32px; top: 32px; font-size: 27px; line-height: 31px; }
  .headline .ask { color: var(--headline); }
  .bullet { padding-left: 22px; width: 500px; }
  .bullet::before {
    content: ""; position: absolute; left: 4px; top: 9px; width: 9px; height: 9px;
    border: 1.3px solid var(--ink); border-radius: 50%;
  }
  .photo { position: absolute; top: 970px; width: 191px; height: 128px; }
  .photo--one { left: 62px; background: linear-gradient(135deg, #6e5a45, #c9a882 55%, #2a2a2a); }
  .photo--two { left: 278px; background: linear-gradient(135deg, #e9ecef, #d7b28c 50%, #8a9aa6); }
  .back-list .bullet { left: 41px; width: 480px; font-size: 22px; line-height: 27px; }
  .back-list .bullet::before { left: 3px; top: 9px; }
  .coach-name {
    position: absolute; left: 19px; top: 638px; font-family: "Josefin Sans", sans-serif;
    font-weight: 300; color: var(--accent); font-size: 27px; letter-spacing: 3px;
  }
  .coach-title {
    position: absolute; left: 19px; top: 670px; font-family: "Josefin Sans", sans-serif;
    font-weight: 300; color: var(--accent); font-size: 18px; letter-spacing: 3.4px;
  }
  .portrait {
    position: absolute; left: 85px; top: 764px; width: 232px; height: 152px;
    background: linear-gradient(90deg, #cfcfcf, #ededed 50%, #d4d4d4);
  }
  .contact { position: absolute; left: 20px; top: 878px; font-size: 19px; line-height: 27px; }
</style>
</head>
<body>
  <section class="panel panel--front">
    <div class="hero" role="img" aria-label="Foto: gelber Kleinwagen mit Koffern auf dem Dach in einem Feld"></div>
    <div class="frame"></div>

    <div class="block headline">
      Wollen Sie<br>
      <span class="ask">Fahrangst überwinden?<br>Panikattacken beim Autofahren loswerden?<br>Oder einfach sicher Autofahren?</span>
    </div>
    <div class="block" style="left:32px;top:166px;">Dann sind Sie hier richtig!<br>Kommt Ihnen eine dieser Situationen bekannt vor?</div>

    <div class="block bullet" style="left:32px;top:240px;">Angst oder Panikattacken begleiten Sie beim Autofahren. Vielleicht vermeiden Sie deshalb das Autofahren komplett. - Sie möchten <span class="hl">angstfrei und/oder ohne Panikattacken</span> fahren.</div>
    <div class="block bullet" style="left:32px;top:364px;">Sie trauen sich das Autofahren nicht (mehr) zu. - Sie wünschen sich, <span class="hl">sicher, entspannt und stressfrei Auto zu fahren.</span></div>
    <div class="block bullet" style="left:32px;top:464px;">Autofahren erleben Sie unter hoher Anspannung und Stress. - Sie wünschen sich, Autofahren <span class="hl">sicher und entspannt</span> zu erleben.</div>
    <div class="block bullet" style="left:32px;top:564px;">Bestimmte Situationen (z.B. Autobahn, Baustellen, Stadtvekehr...) bereiten Ihnen großen Stress. - Sie möchten diese Situationen <span class="hl">souveräner</span> meistern.</div>

    <div class="block" style="left:32px;top:664px;">Das muss nicht so bleiben!</div>
    <div class="block" style="left:32px;top:713px;">3 Schritte zur Lösung:</div>
    <div class="block" style="left:32px;top:763px;">1. Erstgespräch vereinbaren</div>
    <div class="block" style="left:32px;top:812px;">2. Analyse Ihrer individuellen Situation und Zielsetzung</div>
    <div class="block" style="left:32px;top:862px;width:500px;">3. Individuelles Coaching und Training<br>&nbsp;(ggf. Fahrangst-Therapie - als psychotherapeutische Heilpraktikerin bin&nbsp; ich auf Angst- und Panikstörungen spezialisiert)</div>

    <div class="photo photo--one" role="img" aria-label="Foto: lächelnde Frau mit grauem Haar am Steuer eines Cabrios"></div>
    <div class="photo photo--two" role="img" aria-label="Foto: junge Frau schaut aus dem Autofenster und zeigt Daumen hoch"></div>
  </section>

  <section class="panel panel--back">
    <div class="frame"></div>
    <div class="back-list">
      <div class="block bullet" style="top:64px;">über 10 Jahre Erfahrung als <span class="hl">Trainerin und Coach</span> im Bereich <span class="hl">Fahrsicherheit.</span></div>
      <div class="block bullet" style="top:144px;">Als <span class="hl">psychotherapeutische Heilpraktikerin</span> bin ich <span class="hl">auf Angststörungen und Panikattacken spezialisiert.</span></div>
      <div class="block bullet" style="top:224px;"><span class="hl">100 % auf Sie zugeschnitten:</span> ich hole Sie genau dort ab, wo Sie jetzt stehen und unterstütze Sie in <span class="hl">Ihrem Prozess individuell und zielführend.</span></div>
      <div class="block bullet" style="top:331px;">Wenn es Ihnen nicht möglich ist, in meine Praxis nach Neustadt Westfeld zu kommen: Mit der <span class="hl">mobilen Praxis komme ich auch zu Ihnen.</span></div>
      <div class="block bullet" style="top:438px;"><span class="hl">Termine</span> sind auch a<span class="hl">bends und am Wochenende möglich.</span></div>
    </div>

    <div class="coach-name">Carina Lembeck</div>
    <div class="coach-title">Fahrangst-Bewältigungs-Coach</div>

    <div class="portrait" role="img" aria-label="Porträtfoto der Trainerin in weißer Bluse"></div>
    <div class="contact">
      Weitere Informationen finden Sie auf:<br>
      www.fahrangst-frei-coaching.de<br>
      Oder rufen Sie mich einfach an:<br>
      Tel. 0151 23 48 61 70
    </div>
  </section>
</body>
</html>
```